Business Card Design Project

Please create a custom business card for Plume tallying. The logo is attached to this brief.

Questions can be posted on the Discussion Board.

Address :
CEO : Gerhard Moulin
Mobile : +33641927058
9 rue Vasselot
75014 Paris
France

Reason: Sorry wrong logo. I will update asap

Hi, Sorry, I post the wrong file. I just update the correct logo. If you can integrate some charts as background it will be nice

Hi Everybody Please make it beautifull, clean, soft like quince designs does to create their product. I want somewhere to show in a beautifull way some datavisualization charts. Not to much, but try to find a way to design it beautifull with less. Get inspire by datavisualization : http://www.brovaxkit.com/27841-neat-vector-chart-and-graph-layout-pieces-07/

Target Market(s)

B to B
Customers are accountant, CPA, finance departement

Industry/Entity Type

Business

Font styles to use
Sans Serif

Requirements
Must have
• I want to give a clear message about what we do. We do dashboards, we create beautifull charts
Nice to have
• displays charts icons to let people know tha we do charts

```html
<!DOCTYPE html>
<html lang="en">
<head>
<meta charset="utf-8">
<title>Plume tallying — Business Card</title>
<link rel="stylesheet" href="https://fonts.googleapis.com/css2?family=Exo+2:wght@500;600&family=Ubuntu:wght@400&display=swap">
<style>
  :root {
    --backdrop: #e9e6e1;
    --card: #ffffff;
    --brand-blue: #0ea5e4;
    --ink: #2b2b2b;
    --ink-soft: #555555;
    --bar-red: #e31b1b;
    --bar-yellow: #fbbf1f;
    --bar-blue: #00a4e6;
    --bar-green: #22ac38;
  }
  * { box-sizing: border-box; margin: 0; padding: 0; }
  html, body {
    width: 1200px; height: 900px; overflow: hidden;
    background: var(--backdrop);
  }
  .canvas {
    position: relative; width: 1200px; height: 900px;
  }
  .card {
    position: absolute; left: 220px; width: 760px; height: 380px;
    background: var(--card);
    box-shadow: 0 6px 18px rgba(0,0,0,0.18);
    overflow: hidden;
  }
  .card--front { top: 50px; }
  .card--back { top: 470px; }

  .brand {
    position: absolute; display: flex; align-items: center; gap: 14px;
  }
  .brand__square {
    width: 30px; height: 30px; background: var(--brand-blue);
  }
  .brand__name {
    font-family: "Exo 2", sans-serif; font-weight: 500;
    font-size: 40px; color: var(--brand-blue); letter-spacing: 0.5px;
  }
  .card--front .brand { left: 80px; top: 250px; }
  .card--back .brand { left: 80px; top: 170px; }
  .card--back .brand__name { font-size: 34px; }
  .card--back .brand__square { width: 26px; height: 26px; }

  .corner-graphic {
    position: absolute; right: 0; top: 0; width: 250px; height: 110px;
    background: linear-gradient(135deg, #3a8ee8 0%, #1a5fcf 100%);
    opacity: 0.9;
  }

  .divider {
    position: absolute; left: 470px; top: 60px; width: 3px; height: 170px;
    background: linear-gradient(to bottom, rgba(14,165,228,0) 0%, var(--brand-blue) 25%, var(--brand-blue) 70%, rgba(14,165,228,0) 100%);
  }
  .contact {
    position: absolute; left: 500px; top: 62px;
    font-family: "Ubuntu", sans-serif; color: var(--ink);
  }
  .contact__name {
    font-family: "Exo 2", sans-serif; font-weight: 600;
    font-size: 26px; color: var(--brand-blue); line-height: 1.1;
  }
  .contact__role { font-size: 16px; color: var(--ink-soft); margin: 2px 0 16px 14px; }
  .contact__row {
    display: flex; align-items: flex-start; gap: 10px;
    font-size: 17px; line-height: 1.25; margin-bottom: 12px; margin-left: 40px;
  }
  .contact__row svg { flex: none; margin-top: 2px; }

  .bars {
    position: absolute; left: 0; right: 0; bottom: 0; height: 42px;
    display: flex; gap: 12px;
  }
  .bars__segment { flex: 1; }
  .bars__segment--red { background: var(--bar-red); }
  .bars__segment--yellow { background: var(--bar-yellow); }
  .bars__segment--blue { background: var(--bar-blue); }
  .bars__segment--green { background: var(--bar-green); }
</style>
</head>
<body>
<main class="canvas">
  <section class="card card--front" aria-label="Card front">
    <div class="corner-graphic" role="img" aria-label="Decorative brand graphic in blue, green, red and yellow"></div>
    <div class="brand">
      <span class="brand__square"></span>
      <span class="brand__name">Plume tallying</span>
    </div>
  </section>

  <section class="card card--back" aria-label="Card back">
    <div class="brand">
      <span class="brand__square"></span>
      <span class="brand__name">Plume tallying</span>
    </div>
    <div class="divider"></div>
    <div class="contact">
      <p class="contact__name">Gerhard Moulin</p>
      <p class="contact__role">C.E.O.</p>
      <p class="contact__row">
        <svg width="12" height="18" viewBox="0 0 12 18" aria-hidden="true">
          <rect x="1" y="1" width="10" height="16" rx="2" fill="none" stroke="var(--brand-blue)" stroke-width="1.6"/>
          <line x1="4" y1="14" x2="8" y2="14" stroke="var(--brand-blue)" stroke-width="1.4"/>
        </svg>
        <span>+33641927058</span>
      </p>
      <p class="contact__row">
        <svg width="16" height="18" viewBox="0 0 16 18" aria-hidden="true">
          <path d="M8 1a4.5 4.5 0 0 0-4.5 4.5C3.5 9 8 13 8 13s4.5-4 4.5-7.5A4.5 4.5 0 0 0 8 1z" fill="var(--brand-blue)"/>
          <circle cx="8" cy="5.5" r="1.6" fill="#fff"/>
          <ellipse cx="8" cy="15" rx="7" ry="2.2" fill="none" stroke="var(--brand-blue)" stroke-width="1.3"/>
        </svg>
        <span>9 rue Vasselot,<br>75014 Paris, France</span>
      </p>
    </div>
    <div class="bars" aria-hidden="true">
      <span class="bars__segment bars__segment--red"></span>
      <span class="bars__segment bars__segment--yellow"></span>
      <span class="bars__segment bars__segment--blue"></span>
      <span class="bars__segment bars__segment--green"></span>
    </div>
  </section>
</main>
</body>
</html>
```